We are looking for an effective ad to recruit work from home Loan Officers for our Mortgage Brokerage.
Use the following text...
Earn Mortgage Income in your sleep. Its as easy as 1, 2, 3.....
1) Solicit Potential Applicants (Word of Mouth, Email, Social Media etc.)
2) Take Complete Applications & Submit Them
3) Wait to Get Paid.......(Avg. $2,500 per closing)
"You open the door, we'll finish the deal"
No Experience Necessary
No Goals or Quotas
No Office Hours / Work from Home Office
...and We Fully Reimburse ALL LICENSING FEES!!
Email Resume to mwelby@brightharborloans.example
Bright Harbor Lending Group, Inc.
947 W Caldwell Avenue, #318
Baltimore, MD 21230
NMLS #731860
www.brightharborloans.example
Phone (800) 555-0142
Licensed Mortgage Broker in MD and DC since 1997
Target Market(s)
Professionals looking to earn part time income at Loan Officers, preferably with strong social media following.
Industry/Entity Type
Loan
Look and feel

```html
<!DOCTYPE html>
<html lang="en">
<head>
<meta charset="utf-8">
<title>Bright Harbor Lending Group – Loan Officer Recruitment</title>
<link href="https://fonts.googleapis.com/css2?family=Fira+Sans:wght@500;600;700;800&family=Tinos:wght@400;700&display=swap" rel="stylesheet">
<style>
  :root {
    --ink: #111111;
    --header-bg: #0b0b0b;
    --brand-blue: #0a5fa8;
    --olive: #9a8a26;
    --orange: #d0651f;
    --red: #d42a2c;
    --white: #ffffff;
    --paper: #ffffff;
    --skin: #e9c3ae;
    --blouse: #f3d7e4;
    --hair: #5a3226;
  }
  * { margin: 0; padding: 0; box-sizing: border-box; }
  html, body { width: 928px; height: 1200px; overflow: hidden; background: var(--paper); }
  .flyer { position: relative; width: 928px; height: 1200px; background: var(--paper); overflow: hidden; font-family: "Fira Sans", sans-serif; color: var(--ink); }

  .header { position: absolute; left: 0; top: 0; width: 928px; height: 300px; background: var(--header-bg); }
  .headline { position: absolute; top: 44px; left: 0; width: 928px; text-align: center; font-weight: 700; font-size: 58px; line-height: 69px; color: var(--brand-blue); letter-spacing: 0.5px; }
  .headline .n1 { color: var(--olive); }
  .headline .n2 { color: var(--orange); }
  .headline .n3 { color: var(--red); }

  .portrait { position: absolute; left: 548px; top: 277px; width: 380px; height: 760px;
    background: linear-gradient(180deg, var(--hair) 0%, #8c5a48 18%, var(--skin) 38%, var(--blouse) 62%, #f7e6ee 82%, rgba(255,255,255,0) 100%);
    border-radius: 190px 0 0 0; opacity: 0.85; }

  .steps { position: absolute; left: 47px; top: 337px; width: 560px; }
  .step { position: relative; height: 50px; margin-bottom: 25px; }
  .step-band { position: absolute; left: 26px; top: 0; width: 530px; height: 50px; display: flex; flex-direction: column; justify-content: center; padding-left: 52px; font-family: "Tinos", serif; font-weight: 700; color: var(--white); font-size: 16px; line-height: 18px; letter-spacing: 0.2px; }
  .step-band small { font-weight: 400; font-size: 14px; }
  .step-num { position: absolute; left: 0; top: -2px; width: 54px; height: 54px; border-radius: 50%; display: flex; align-items: center; justify-content: center; font-family: "Tinos", serif; font-size: 40px; color: var(--white); box-shadow: 0 2px 4px rgba(0,0,0,0.35); }
  .step-1 .step-band, .step-1 .step-num { background: var(--olive); }
  .step-2 .step-band, .step-2 .step-num { background: var(--orange); }
  .step-3 .step-band, .step-3 .step-num { background: var(--red); }

  .motto { position: absolute; left: 57px; top: 596px; font-weight: 700; font-size: 35px; line-height: 46px; color: var(--brand-blue); }

  .perks { position: absolute; left: 62px; top: 734px; list-style: none; font-weight: 500; font-size: 20px; line-height: 27px; }
  .perks li { display: flex; align-items: center; gap: 10px; }
  .perks svg { width: 17px; height: 15px; }

  .reimburse { position: absolute; left: 57px; top: 845px; font-weight: 500; font-size: 20px; }

  .brand { position: absolute; left: 40px; top: 1010px; display: flex; align-items: center; gap: 16px; }
  .brand-dot { width: 52px; height: 52px; border-radius: 50%; background: var(--brand-blue); }
  .brand-name { font-weight: 700; font-size: 24px; color: var(--brand-blue); line-height: 30px; }

  .contact { position: absolute; left: 462px; top: 1006px; font-weight: 500; font-size: 15.5px; line-height: 20.5px; }
  .contact .email { margin-bottom: 10px; }
  .license { position: absolute; left: 462px; top: 1146px; font-family: "Tinos", serif; font-size: 13.5px; letter-spacing: 0.2px; }
</style>
</head>
<body>
<main class="flyer">
  <header class="header">
    <h1 class="headline">EARN MORTGAGE INCOME<br>IN YOUR SLEEP.<br>ITS AS EASY AS <span class="n1">1,</span> <span class="n2">2,</span> <span class="n3">3.....</span></h1>
  </header>

  <div class="portrait" role="img" aria-label="Smiling woman pointing up and holding a fan of dollar bills"></div>

  <section class="steps">
    <div class="step step-1"><div class="step-band">SOLICIT POTENTIAL APPLICANTS<small>(WORD OF MOUTH, EMAIL, SOCIAL MEDIA ETC.)</small></div><div class="step-num">1</div></div>
    <div class="step step-2"><div class="step-band">TAKE COMPLETE APPLICATIONS &amp; SUBMIT THEM</div><div class="step-num">2</div></div>
    <div class="step step-3"><div class="step-band">WAIT TO GET PAID.......(AVG. $2,500 PER CLOSING)</div><div class="step-num">3</div></div>
  </section>

  <p class="motto">"YOU OPEN THE DOOR,<br>WE'LL FINISH THE DEAL"</p>

  <ul class="perks">
    <li><svg viewBox="0 0 17 15"><path d="M1 8 L6 13 L16 2" fill="none" stroke="#111" stroke-width="3"/></svg>NO EXPERIENCE NECESSARY</li>
    <li><svg viewBox="0 0 17 15"><path d="M1 8 L6 13 L16 2" fill="none" stroke="#111" stroke-width="3"/></svg>NO GOALS OR QUOTAS</li>
    <li><svg viewBox="0 0 17 15"><path d="M1 8 L6 13 L16 2" fill="none" stroke="#111" stroke-width="3"/></svg>NO OFFICE HOURS / WORK FROM HOME OFFICE</li>
  </ul>

  <p class="reimburse">...AND WE FULLY REIMBURSE ALL LICENSING FEES!!</p>

  <div class="brand">
    <div class="brand-dot"></div>
    <div class="brand-name">Bright Harbor<br>Lending Group, Inc.</div>
  </div>

  <address class="contact" style="font-style:normal">
    <div class="email">Email Resume to mwelby@brightharborloans.example</div>
    <div>Bright Harbor Lending Group, Inc.</div>
    <div>947 W Caldwell Avenue, #318 Baltimore,</div>
    <div>MD 21230, NMLS #731860</div>
    <div>www.brightharborloans.example | Phone (800) 555-0142</div>
  </address>

  <p class="license">LICENSED MORTGAGE BROKER IN MD AND DC SINCE 1997</p>
</main>
</body>
</html>
```